Oven Cleaning Business owner needs business card design

Hi there,
Would like for a business card to be designed for myself, the owner of a professional oven cleaning business on the Sunshine Coast.
Would like it to look sleek, and modern-ish. Bit creative is encouraged too.
Include following:
Name/title: Corin ter Haghe, Owner
Phone number: 1300 482 916
Email: info@hearthshinecrew.com.au
Website: www.hearthshinecrew.com.au

```html
<!DOCTYPE html>
<html lang="en">
<head>
<meta charset="utf-8">
<title>Hearthshine Crew – Business Card</title>
<link href="https://fonts.googleapis.com/css2?family=Michroma&family=Open+Sans:wght@400;600&display=swap" rel="stylesheet">
<style>
  :root {
    --backdrop: #d3d4d6;
    --steel-dark: #303031;
    --steel-mid: #6a6a6c;
    --steel-light: #a3a3a5;
    --ink: #111111;
    --aqua: #1bdfe0;
    --paper: #ffffff;
    --text: #1a1a1a;
  }
  * { box-sizing: border-box; margin: 0; padding: 0; }
  html, body {
    width: 900px; height: 1200px; overflow: hidden;
    background: var(--backdrop);
  }
  .canvas { position: relative; width: 900px; height: 1200px; }

  .card {
    position: absolute;
    width: 626px; height: 368px;
    background: linear-gradient(90deg, var(--steel-dark) 0%, var(--steel-mid) 25%, var(--steel-light) 50%, var(--steel-mid) 75%, var(--steel-dark) 100%);
  }
  .card--front { left: 138px; top: 194px; }
  .card--back  { left: 137px; top: 625px; }

  .card__rail {
    position: absolute; left: 0; right: 0; top: 46px; height: 4px;
    background: var(--ink);
  }
  .card__display {
    position: absolute; left: 30px; top: 9px; width: 118px; height: 28px;
    background: var(--ink); border: 1px solid var(--aqua);
  }
  .card__knob {
    position: absolute; top: 8px; width: 31px; height: 31px; border-radius: 50%;
    background: var(--ink); border: 1px solid var(--aqua);
  }
  .card__knob--left  { left: 524px; }
  .card__knob--right { left: 563px; }

  .card__window {
    position: absolute; left: 30px; top: 73px; width: 565px; height: 256px;
    background: var(--paper); border: 1px solid var(--aqua);
  }

  .brand {
    display: flex; align-items: center; gap: 14px;
    font-family: "Michroma", sans-serif; color: var(--ink);
  }
  .brand__dot { border-radius: 50%; background: var(--aqua); flex: none; }

  .card--front .brand {
    position: absolute; inset: 0; justify-content: center;
    font-size: 27px; letter-spacing: 1px;
  }
  .card--front .brand__dot { width: 54px; height: 54px; }

  .card--back .brand {
    position: absolute; right: 40px; bottom: 44px;
    flex-direction: column; gap: 12px; text-align: center;
    font-size: 15px; letter-spacing: 1px;
  }
  .card--back .brand__dot { width: 70px; height: 70px; }

  .owner { position: absolute; left: 40px; top: 40px; }
  .owner__name {
    font-family: "Michroma", sans-serif; font-size: 17px; color: var(--aqua);
    font-weight: 400; letter-spacing: -0.3px;
  }
  .owner__role {
    font-family: "Open Sans", sans-serif; font-size: 15px; color: var(--text);
    letter-spacing: 1px; margin-top: 2px;
  }

  .contact {
    position: absolute; left: 40px; top: 140px; list-style: none;
    font-family: "Open Sans", sans-serif; font-size: 15px; color: var(--text);
    letter-spacing: 0.8px;
  }
  .contact__item { display: flex; align-items: center; gap: 5px; height: 25.5px; }
  .contact__icon { width: 13px; height: 13px; flex: none; }
</style>
</head>
<body>
<div class="canvas">

  <section class="card card--front" aria-label="Card front">
    <div class="card__display"></div>
    <div class="card__knob card__knob--left"></div>
    <div class="card__knob card__knob--right"></div>
    <div class="card__rail"></div>
    <div class="card__window">
      <div class="brand">
        <span class="brand__dot"></span>
        <span class="brand__name">HEARTHSHINE CREW</span>
      </div>
    </div>
  </section>

  <section class="card card--back" aria-label="Card back">
    <div class="card__display"></div>
    <div class="card__knob card__knob--left"></div>
    <div class="card__knob card__knob--right"></div>
    <div class="card__rail"></div>
    <div class="card__window">
      <div class="owner">
        <h1 class="owner__name">Corin ter Haghe</h1>
        <p class="owner__role">Owner</p>
      </div>
      <ul class="contact">
        <li class="contact__item">
          <svg class="contact__icon" viewBox="0 0 16 16" aria-hidden="true"><path fill="#1bdfe0" d="M3.6 1.2l2.3 2.9-1.4 1.7c.9 2 2.5 3.6 4.5 4.6l1.7-1.4 2.9 2.3-1.3 2.6C7.4 13.6 2.3 8.5 1 3z"/></svg>
          <span>1300 482 916</span>
        </li>
        <li class="contact__item">
          <svg class="contact__icon" viewBox="0 0 16 16" aria-hidden="true"><rect x="1" y="3" width="14" height="10" fill="#1bdfe0"/><path d="M1 3l7 6 7-6M1 13l5-4.5M15 13l-5-4.5" stroke="#fff" stroke-width="1.2" fill="none"/></svg>
          <span>info@hearthshinecrew.com.au</span>
        </li>
        <li class="contact__item">
          <svg class="contact__icon" viewBox="0 0 16 16" aria-hidden="true"><g fill="none" stroke="#1bdfe0" stroke-width="1.3"><circle cx="8" cy="8" r="6.5"/><ellipse cx="8" cy="8" rx="3" ry="6.5"/><path d="M1.5 8h13M2.5 4.8h11M2.5 11.2h11"/></g></svg>
          <span>www.hearthshinecrew.com.au</span>
        </li>
      </ul>
      <div class="brand">
        <span class="brand__dot"></span>
        <span class="brand__name">HEARTHSHINE<br>CREW</span>
      </div>
    </div>
  </section>

</div>
</body>
</html>
```